Food delivery wordpress design

need food delivery wordpress design for my site, here's the requirements
1. site must be pixel perfect , clean and professional
2. logo provided and must be match with the color scheme
3. pages : home , about us , faq , vendor registration

*** this is a information site no order can be made from the site, the site will show how things work , how to register as vendor , how to use the app , you may use any stock photo from pictorvane and send me the code, i will purchase it

you may use any of the logo to play with it

***** It must look scale and not looks like template where I can purchase elsewhere

the designer told me he can't work as he got his personal problem, please check his message

those who prefer to purchase online

Sans Serif

• refer to zelvo.com/my
• everything user and vendor like to know

```html
<!DOCTYPE html>
<html lang="en">
<head>
<meta charset="utf-8">
<title>makanlaju — Food Delivery</title>
<link href="https://fonts.googleapis.com/css2?family=Fira+Sans:wght@400;500;600;700&family=Montserrat:wght@400;700&display=swap" rel="stylesheet">
<style>
:root{
  --orange:#f29f24;
  --orange-deep:#e9921a;
  --cream:#fdecd3;
  --ink:#2f2f2e;
  --text:#3b3b3b;
  --muted:#555;
  --footer:#333230;
  --white:#fff;
}
*{margin:0;padding:0;box-sizing:border-box}
html,body{width:1200px;height:4232px;overflow:hidden}
body{position:relative;font-family:"Fira Sans",sans-serif;color:var(--text);background:var(--white)}
.abs{position:absolute}

/* header */
.site-header{position:absolute;left:0;top:0;width:1200px;height:107px;background:var(--white)}
.brand{position:absolute;display:flex;align-items:center;gap:10px;font-family:"Fira Sans",sans-serif;font-weight:600;color:var(--ink)}
.brand .dot{width:34px;height:34px;border-radius:50%;background:var(--orange)}
.site-header .brand{left:112px;top:36px;font-size:36px}
.nav{position:absolute;top:54px;font-size:14px;font-weight:500;color:var(--ink);letter-spacing:.3px;transform:translateX(-50%)}
.nav.active::after{content:"";position:absolute;left:50%;top:24px;width:20px;height:3px;background:var(--ink);transform:translateX(-50%);box-shadow:4px 6px 0 -0px var(--ink)}

/* hero */
.hero{position:absolute;left:0;top:107px;width:1200px;height:600px;background:linear-gradient(120deg,#f2a52c,#e8951c 60%,#efa02a)}
.hero-art{position:absolute;left:0;top:82px;width:545px;height:545px;border-radius:40% 50% 45% 40%;background:radial-gradient(circle at 55% 55%,#f7a32a,#f19a20 55%,transparent 70%)}
.hero h1{position:absolute;left:603px;top:135px;width:560px;font-size:49px;line-height:54px;font-weight:700;color:var(--ink)}
.hero p{position:absolute;left:603px;top:316px;width:470px;font-size:16px;line-height:30px;color:#3a2c14}
.btn{position:absolute;display:flex;align-items:center;justify-content:center;border-radius:30px;font-weight:600;font-size:17px}
.btn-dark{left:602px;top:398px;width:215px;height:59px;background:var(--ink);color:var(--white);border:3px solid var(--white);box-shadow:0 3px 6px rgba(0,0,0,.25)}

/* about */
.about{position:absolute;left:0;top:707px;width:1200px;height:480px;background:var(--cream);text-align:center}
.section-title{font-size:36px;font-weight:600;color:var(--ink)}
.section-title .hl{color:var(--orange)}
.rule{width:60px;height:4px;background:var(--orange);margin:0 auto}
.about .section-title{position:absolute;left:0;right:0;top:108px}
.about .rule{position:absolute;left:570px;top:168px}
.about p{position:absolute;left:148px;top:190px;width:904px;font-size:15px;line-height:30px;color:var(--text)}
.btn-orange{left:501px;top:330px;width:198px;height:53px;background:var(--orange);color:var(--ink);border:3px solid var(--ink);box-shadow:0 3px 6px rgba(0,0,0,.2)}

/* feature rows */
.feature h2{position:absolute;font-size:36px;font-weight:600;color:var(--ink)}
.feature h2 .hl{color:var(--orange)}
.feature p{position:absolute;width:420px;font-size:15px;line-height:30px;color:var(--text)}
.btn-outline{width:199px;height:55px;border:3px solid var(--ink);color:var(--ink);background:var(--white);box-shadow:0 3px 6px rgba(0,0,0,.2)}
.photo{position:absolute;width:464px;height:492px;box-shadow:0 4px 12px rgba(0,0,0,.2)}

/* faq */
.faq{position:absolute;left:0;top:2882px;width:1200px;height:801px;background:linear-gradient(160deg,#f0a22a,#e8951e 50%,#f0a02a)}
.faq .section-title{position:absolute;left:0;right:0;top:98px;text-align:center}
.faq .rule{position:absolute;left:570px;top:154px}
.faq-list{position:absolute;left:194px;top:202px;width:812px;background:var(--white);border:1px solid #ddd}
.faq-q{height:75px;display:flex;align-items:center;justify-content:space-between;padding:0 22px;font-size:16px;font-weight:500;color:var(--ink);border-top:2px solid #e4e4e4}
.faq-q:first-child{border-top:none;height:72px;border-bottom:1px solid #e4e4e4}
.faq-q .plus{font-size:18px;font-weight:700}
.faq-a{height:130px;padding:22px 20px 0;font-size:12.5px;line-height:30px;color:var(--muted)}

/* footer */
.footer{position:absolute;left:0;top:3683px;width:1200px;height:549px;background:var(--footer);color:var(--white)}
.mail-title{position:absolute;left:0;right:0;top:60px;text-align:center;font-family:"Montserrat",sans-serif;font-weight:700;font-size:34px;color:var(--white)}
.mail-sub{position:absolute;left:0;right:0;top:118px;text-align:center;font-family:"Montserrat",sans-serif;font-size:12.5px}
.mail-form{position:absolute;left:233px;top:161px;width:642px;height:52px;background:var(--white);border-radius:30px}
.mail-form span{position:absolute;left:48px;top:18px;font-family:"Montserrat",sans-serif;font-size:11px;color:#999}
.mail-form .submit{position:absolute;right:0;top:0;width:140px;height:52px;border-radius:30px;background:var(--orange);border:2px solid var(--white);display:flex;align-items:center;justify-content:center;font-family:"Montserrat",sans-serif;font-size:16px;color:var(--white)}
.footer hr{position:absolute;left:66px;top:244px;width:978px;border:none;border-top:1px solid #777}
.footer .brand{left:41px;top:304px;font-size:34px;color:var(--white)}
.social{position:absolute;top:401px;width:32px;height:32px;border-radius:50%;background:var(--orange);border:3px solid var(--white)}
.col{position:absolute;top:286px;font-family:"Montserrat",sans-serif}
.col h4{font-size:17px;font-weight:700;margin-bottom:14px}
.col li{list-style:none;font-size:14px;line-height:29.5px;padding-left:24px;position:relative}
.col li::before{content:"»";position:absolute;left:6px}
.contact-row{position:absolute;font-family:"Montserrat",sans-serif;font-size:14px;line-height:29.5px;display:flex;gap:14px}
.contact-row svg{flex:none;margin-top:7px}
.copyright{position:absolute;left:79px;top:495px;font-family:"Montserrat",sans-serif;font-size:12.5px}
</style>
</head>
<body>

<header class="site-header">
  <div class="brand"><span class="dot"></span>makanlaju</div>
  <span class="nav active" style="left:473px">HOME</span>
  <span class="nav" style="left:569px">ABOUT US</span>
  <span class="nav" style="left:656px">FAQ</span>
  <span class="nav" style="left:791px">VENDOR REGISTRATION</span>
  <span class="nav" style="left:957px">CONTACT US</span>
  <svg class="abs" style="left:1063px;top:55px" width="14" height="14" viewBox="0 0 14 14"><circle cx="6" cy="6" r="4.5" fill="none" stroke="#2f2f2e" stroke-width="2"/><line x1="9.3" y1="9.3" x2="13" y2="13" stroke="#2f2f2e" stroke-width="2.2"/></svg>
</header>

<section class="hero">
  <div class="hero-art" role="img" aria-label="Mascot illustration of a running chef bird over a photo of fresh market produce"></div>
  <h1>Lorem Ipsum Dolor Sit Amet, Consectetur Ad Ipiscing Elit Sed</h1>
  <p>Lorem ipsum dolor sit amet, consectetur adipiscing elit, sed do eiusmod tempor incididunt ut labore et.</p>
  <div class="btn btn-dark">Get Started</div>
</section>

<section class="about">
  <h2 class="section-title"><span class="hl">About</span> Makanlaju</h2>
  <div class="rule"></div>
  <p>Lorem ipsum dolor sit amet, consectetur adipiscing elit, sed do eiusmod tempor incididunt ut labore et dolore magna aliqua. Ut enim ad minim veniam, quis nostrud exercitation ullamco laboris nisi ut aliquip ex ea commodo consequat. Duis aute irure dolor in reprehenderit in voluptate velit esse cillum dolore eu fugiat nulla pariatur. Excepteur sint occaecat cupidatat non proident, sunt in culpa qui officia deserunt mollit anim id est laborum.</p>
  <div class="btn btn-orange">Learn More</div>
</section>

<section class="feature">
  <h2 style="left:110px;top:1358px">How <span class="hl">Things Work</span></h2>
  <p style="left:110px;top:1420px">Lorem ipsum dolor sit amet, consectetur adipiscing elit, sed do eiusmod tempor incididunt ut labore et dolore magna aliqua. Ut enim ad minim veniam, quis nostrud exercitation ullamco laboris nisi ut aliquip ex ea commodo consequat. Duis aute irure dolor in reprehenderit in voluptate velit esse cillum dolore eu fugiat nulla pariatur.</p>
  <div class="btn btn-outline" style="left:110px;top:1619px">Learn More</div>
  <div class="photo" style="left:625px;top:1274px;background:linear-gradient(100deg,#1f4a5c 0%,#2b6a7c 30%,#b08a5c 50%,#e8e4de 75%,#d9b56a 100%)" role="img" aria-label="Photo of a paper food delivery bag being handed to a customer holding a phone"></div>

  <div class="photo" style="left:110px;top:1766px;background:linear-gradient(100deg,#1d3b32 0%,#284a40 35%,#cfc6bb 60%,#e6e2dc 100%)" role="img" aria-label="Photo of a smiling woman receiving a cardboard parcel at her door"></div>
  <h2 style="left:659px;top:1850px">How To <span class="hl">Register as a Vendor</span></h2>
  <p style="left:659px;top:1912px">Lorem ipsum dolor sit amet, consectetur adipiscing elit, sed do eiusmod tempor incididunt ut labore et dolore magna aliqua. Ut enim ad minim veniam, quis nostrud exercitation ullamco laboris nisi ut aliquip ex ea commodo consequat. Duis aute irure dolor in reprehenderit in voluptate velit esse cillum dolore eu fugiat nulla pariatur.</p>
  <div class="btn btn-outline" style="left:659px;top:2111px">Learn More</div>

  <h2 style="left:110px;top:2341px">How To <span class="hl">Use The App</span></h2>
  <p style="left:110px;top:2403px">Lorem ipsum dolor sit amet, consectetur adipiscing elit, sed do eiusmod tempor incididunt ut labore et dolore magna aliqua. Ut enim ad minim veniam, quis nostrud exercitation ullamco laboris nisi ut aliquip ex ea commodo consequat. Duis aute irure dolor in reprehenderit in voluptate velit esse cillum dolore eu fugiat nulla pariatur.</p>
  <div class="btn btn-outline" style="left:110px;top:2601px">Download The App</div>
  <div class="photo" style="left:625px;top:2257px;background:linear-gradient(110deg,#cfc9c2 0%,#e9e6e1 45%,#f2a024 70%,#d9c3ae 100%)" role="img" aria-label="Photo of a hand holding a smartphone showing the app's orange start screen"></div>
</section>

<section class="faq" role="region" aria-label="Frequently Asked Questions">
  <h2 class="section-title">Frequently Asked Questions</h2>
  <div class="rule" style="background:var(--ink)"></div>
  <div class="faq-list">
    <div class="faq-q">Lorem ipsum dolor sit amet, consectetur adipiscing elit ?<span class="plus">+</span></div>
    <div class="faq-a">Lorem ipsum dolor sit amet, consectetur adipiscing elit, sed do eiusmod tempor incididunt ut labore et dolore magna aliqua. Ut enim ad minim veniam, quis nostrud exercitation ullamco laboris nisi ut aliquip ex ea commodo consequat. Duis aute irure dolor in reprehenderit in voluptate velit esse cillum dolore eu fugiat nulla</div>
    <div class="faq-q">Lorem ipsum dolor sit amet, consectetur adipiscing elit ?<span class="plus">+</span></div>
    <div class="faq-q">Lorem ipsum dolor sit amet, consectetur adipiscing elit ?<span class="plus">+</span></div>
    <div class="faq-q">Lorem ipsum dolor sit amet, consectetur adipiscing elit ?<span class="plus">+</span></div>
    <div class="faq-q">Lorem ipsum dolor sit amet, consectetur adipiscing elit ?<span class="plus">+</span></div>
  </div>
</section>

<footer class="footer">
  <h2 class="mail-title">JOIN OUR MAILING LIST</h2>
  <p class="mail-sub">Lorem ipsum dolor sit amet, consectetur adipiscing elit, sed do eiusmod tempor</p>
  <div class="mail-form"><span>Enter Email Here</span><div class="submit">SUBMIT</div></div>
  <hr>
  <div class="brand"><span class="dot"></span>makanlaju</div>
  <span class="social" style="left:79px"></span>
  <span class="social" style="left:127px"></span>
  <span class="social" style="left:175px"></span>
  <span class="social" style="left:222px"></span>

  <div class="col" style="left:349px"><h4>QUICK LINKS</h4><ul><li>Home</li><li>About us</li><li>FAQ</li><li>Vendor Registration</li></ul></div>
  <div class="col" style="left:602px"><h4>LEGAL</h4><ul><li>Terms of Use</li><li>Privacy Policy</li><li>Contact Us</li><li>FAQ</li></ul></div>
  <div class="col" style="left:820px"><h4>CONTACT US</h4></div>
  <div class="contact-row" style="left:828px;top:327px;width:300px">
    <svg width="12" height="16" viewBox="0 0 12 16"><path d="M6 0C2.7 0 0 2.6 0 5.9 0 10.3 6 16 6 16s6-5.7 6-10.1C12 2.6 9.3 0 6 0zm0 8.2A2.3 2.3 0 1 1 6 3.6a2.3 2.3 0 0 1 0 4.6z" fill="#fff"/></svg>
    <span>123 Lorem ipsum dolor sit amet, consectetur adipiscing elit</span>
  </div>
  <div class="contact-row" style="left:828px;top:396px">
    <svg width="14" height="14" viewBox="0 0 14 14"><path d="M3 0l2.5 3.3-1.6 1.8a9 9 0 0 0 5 5l1.8-1.6L14 11l-2 3C5.5 13.5.5 8.5 0 2z" fill="#fff"/></svg>
    <span>123 456 7890</span>
  </div>
  <div class="contact-row" style="left:828px;top:439px">
    <svg width="15" height="11" viewBox="0 0 15 11"><rect width="15" height="11" fill="#fff"/><path d="M0 0l7.5 6L15 0" fill="none" stroke="#333230" stroke-width="1.4"/></svg>
    <span>info@makanlaju.com</span>
  </div>
  <p class="copyright">© Copyrights 2021 MAKANLAJU &nbsp; | &nbsp; All Rights Reserved</p>
</footer>

</body>
</html>
```